Career development coaching - school lever to adults, needs a business card

Tandem Lark - An independent Career Advice business that provides 1-2-1 advice,for career development, entrepreneurial support and workshops needs a business card. Our clients of all ages (school leaver to adults looking for a career move) and universities and colleges. We would like the card to be double-sided with a modern, professional look. Looking for something professional yet very creative and original. Want a standard size business card that inspires a second look because it stands out from the rest.

One side of the card to have a design incorporating the logo with Tandem Lark name with the strap line “Guiding every step of your career” and space for the company website

Other side of the card to the logo/Tandem Lark name and the usual contact information:
Individual Name
Job Title (for example, Director)
Phone number
Email address
Company website address

Facebook, LinkedIn and Twitter links will need to go somewhere (back or front!)

The design will be used for 3 individuals so should be editable so that we can update as needed/as we grow.

Attached is the company logo/colours to be incorporated.

Target Market(s)

1-2-1 advice,for career development, entrepreneurial support and workshops needs a business card. Our clients of all ages (school leaver to adults looking for a career move) and universities and colleges.

Industry/Entity Type

Consulting

Contact Information for Business Card

Individual Name
Phone number
Email address
Company website address

Font styles to use
Sans Serif

Colors
0255a3
3176b5
faa54b
f78f20
85acd3
cfdeed

Requirements
Must have
• use the Tandem Lark Logo in some way - using the colours and the blue/orange palette
• For the logo - hope this makes sense to someone or if they direclty relate to the logo image attached!
• For the Orange:- Pantone 1585 C
• In CMYK : C3 M71 Y100 K0
• For the Blue:- 100% Pantone 7469 C
• In CMYK : C100 M62 Y27 K7
• Please feel free to contact me with any questions for more info
Nice to have
• happy to see any creative designs
Should not have
• Nothing too traditional,

```html
<!DOCTYPE html>
<html lang="en">
<head>
<meta charset="utf-8">
<title>Tandem Lark – Business Card</title>
<link rel="stylesheet" href="https://fonts.googleapis.com/css2?family=Open+Sans:wght@400;600;700&display=swap">
<style>
  :root {
    --bg: #e4e6ea;
    --card-dark: #353234;
    --card-light: #ffffff;
    --orange: #f07a30;
    --blue: #1f6fa8;
    --ink: #2b2b2b;
    --muted: #d8d6d4;
  }
  * { box-sizing: border-box; margin: 0; padding: 0; }
  html, body { width: 1200px; height: 900px; overflow: hidden; }
  body {
    background: var(--bg);
    font-family: "Open Sans", Arial, sans-serif;
    position: relative;
  }
  .card {
    position: absolute;
    left: 250px;
    width: 700px;
    height: 400px;
    border-radius: 26px;
    overflow: hidden;
    box-shadow: 0 8px 24px rgba(0,0,0,.18);
  }
  /* ---------- front ---------- */
  .card--front { top: 40px; background: var(--card-light); }
  .rule { position: absolute; height: 7px; background: var(--orange); }
  .rule--left { left: 0; top: 140px; width: 230px; }
  .rule--right { right: 0; top: 262px; width: 220px; }
  .brand {
    position: absolute; left: 0; right: 0; top: 156px;
    text-align: center;
  }
  .brand__mark {
    display: inline-flex; align-items: center; gap: 12px;
    font-weight: 700; font-size: 34px; letter-spacing: 1px;
    line-height: 1.1;
    color: var(--blue); text-transform: uppercase;
  }
  .brand__dot {
    width: 30px; height: 30px; border-radius: 50%;
    background: var(--orange); flex: none;
  }
  .brand__tagline {
    margin-top: 8px;
    font-size: 14px; font-weight: 400; letter-spacing: 1.5px;
    color: var(--ink); text-transform: uppercase;
  }
  .social {
    position: absolute; left: 232px; top: 268px;
    display: flex; align-items: center; gap: 8px;
    font-size: 14px; font-weight: 600; color: var(--blue);
  }
  .social__dot { width: 16px; height: 16px; border-radius: 50%; background: var(--blue); }

  /* ---------- back ---------- */
  .card--back { top: 460px; background: var(--card-dark); }
  .tab { position: absolute; left: 0; top: 36px; width: 52px; height: 58px; background: var(--orange); }
  .band { position: absolute; left: 330px; right: 0; top: 104px; height: 66px; background: var(--orange); }
  .person { position: absolute; left: 70px; top: 34px; color: #fff; }
  .person__name { font-size: 32px; font-weight: 600; letter-spacing: 2px; text-transform: uppercase; line-height: 1.1; }
  .person__role { font-size: 20px; font-weight: 400; letter-spacing: 1px; text-align: right; margin-top: 2px; }
  .contact {
    position: absolute; left: 34px; top: 232px;
    list-style: none; color: var(--muted);
    font-size: 15px; line-height: 1;
  }
  .contact li { display: flex; align-items: center; gap: 12px; margin-bottom: 14px; white-space: nowrap; }
  .contact svg { width: 16px; height: 16px; flex: none; }
  .brand--back {
    position: absolute; right: 48px; bottom: 44px;
    display: flex; align-items: center; gap: 10px;
    font-weight: 700; font-size: 26px; letter-spacing: 1px;
    color: var(--blue); text-transform: uppercase; white-space: nowrap;
  }
  .brand--back .brand__dot { width: 24px; height: 24px; }
</style>
</head>
<body>

<section class="card card--front" aria-label="Card front">
  <div class="rule rule--left"></div>
  <div class="rule rule--right"></div>
  <div class="brand">
    <div class="brand__mark"><span class="brand__dot"></span>Tandem Lark</div>
    <p class="brand__tagline">Guiding every step of your career</p>
  </div>
  <div class="social"><span class="social__dot"></span>@tandemlark</div>
</section>

<section class="card card--back" aria-label="Card back">
  <div class="tab"></div>
  <div class="band"></div>
  <div class="person">
    <p class="person__name">Nadia Ferrow</p>
    <p class="person__role">Director</p>
  </div>
  <ul class="contact">
    <li>
      <svg viewBox="0 0 16 16" fill="none" stroke="#f07a30" stroke-width="1.4"><path d="M3 2h3l1 3-2 1.5a9 9 0 0 0 4.5 4.5L11 9l3 1v3a1 1 0 0 1-1 1A11 11 0 0 1 2 3a1 1 0 0 1 1-1z"/></svg>
      +000 5550 1472
    </li>
    <li>
      <svg viewBox="0 0 16 16" fill="none" stroke="#f07a30" stroke-width="1.4"><rect x="1.5" y="3.5" width="13" height="9" rx="1"/><path d="M1.5 4l6.5 5 6.5-5"/></svg>
      nadia@tandemlark.co
    </li>
    <li>
      <svg viewBox="0 0 16 16" fill="none" stroke="#f07a30" stroke-width="1.4"><circle cx="8" cy="8" r="6.5"/><path d="M1.5 8h13M8 1.5c-3 3.5-3 9.5 0 13M8 1.5c3 3.5 3 9.5 0 13"/></svg>
      tandemlark.co
    </li>
    <li>
      <svg viewBox="0 0 16 16" fill="none" stroke="#f07a30" stroke-width="1.4"><path d="M8 15s5-5 5-8.5a5 5 0 0 0-10 0C3 10 8 15 8 15z"/><circle cx="8" cy="6.5" r="1.8"/></svg>
      18 Quill Row, Harbourside, 4821
    </li>
  </ul>
  <div class="brand--back"><span class="brand__dot"></span>Tandem Lark</div>
</section>

</body>
</html>
```